依頼詳細
①TOPページのデザイン案をご提案ください。
②採用させていただく可能性の高い方と、
下層ページ1ページ、採用サイト等別サイト2ページ分について
ご相談したいと考えております。

<サイト概要>
・4ページ分(トップページ、下層ページ、採用サイト等2サイト)
・レスポンシブ
・セミナー案内などを、wordpressで更新していきます。

<納品物>
デザインカンプ(PSD希望ですが、AIでも可)を納品してください。

<応募条件>
・継続依頼も検討しているため、連絡がスムーズな方。

<参考サイト>
・株式会社ペネムス・ヤカルト
http://www.pnm-example.co.jp/

上記サイトのように、ファーストビューに背景に動画をフルスクリーンで表示させるのを希望しています。

・ツクリエ採用サイト
https://www.tsukurie-example.jp/saiyou/service/business.html

<提供する素材>
・写真、ロゴ、サイト内で使用するテキスト
サイトURL
http://www.meadowpath-x.com/
ページ数
4ページ
希望イメージ
シンプル 複雑
単色 カラフル
暗い 明るい
日常 高級
遊び心 厳粛
未来的 伝統的
女性的 男性的
希望する色
設定なし
納品ファイル
• イラストレーター形式 (.ai)
• フォトショップ形式 (.psd)
補足説明
・イラストレーター、フォトショップ、どちらで作成していただいても構いません。最終的に、制作データ(ai or psd)で納品をしていただける方。
・クライアント企業とのコミュニケーションに慣れていて、細かい修正等に対応していただける方
提供する素材を添付させていただきますので、
こちらをご使用ください。

<提供する素材>
・写真、ロゴ、サイト内で使用するテキスト
募集の締め切りを延長しましたので、
引き続きご提案をお待ちしております。
■ 選んだ理由

私たちのイメージに一番近いデザインを出していただきました。
またこちらの意向を汲んでくださり、
今後も引き続きお願いしたいと感じましたので決めさせていただきました。

■ 提案者全員のお礼・コメント

皆様、数々のご提案をいただき、ありがとうございました。

```html
<!DOCTYPE html>
<html lang="ja">
<head>
<meta charset="utf-8">
<title>Meadowpath | 歯科医院専門コンサルティング</title>
<link href="https://fonts.googleapis.com/css2?family=Noto+Sans+JP:wght@400;500;700&family=Noto+Serif+JP:wght@500;700&display=swap" rel="stylesheet">
<style>
:root{
  --green:#5bb531;
  --green-dark:#3f9320;
  --pink:#e2457c;
  --ink:#333;
  --muted:#777;
  --line:#d9d9d9;
  --pale:#f4f4f4;
  --white:#fff;
}
*{box-sizing:border-box;margin:0;padding:0}
html,body{width:1200px;height:4968px;overflow:hidden}
body{font-family:"Noto Sans JP",sans-serif;color:var(--ink);background:var(--white);position:relative}
.serif{font-family:"Noto Serif JP",serif}
.ph{position:absolute;display:block}

/* header */
.site-header{position:absolute;top:0;left:0;width:1200px;height:60px;background:rgba(255,255,255,.95);display:flex;align-items:center;padding:0 0 0 24px;z-index:2}
.brand{display:flex;align-items:center;gap:8px;font-weight:700;color:var(--green);font-size:20px}
.brand-dot{width:18px;height:18px;border-radius:50%;background:var(--green)}
.global-nav{display:flex;gap:30px;margin-left:auto;margin-right:30px;font-size:14px}
.phone-box{width:190px;height:60px;background:var(--green);color:#fff;display:flex;flex-direction:column;justify-content:center;align-items:center}
.phone-box small{font-size:10px}
.phone-box strong{font-size:22px;letter-spacing:1px}

.hero{left:0;top:0;width:1200px;height:672px;background:linear-gradient(120deg,#e8e4dc 0%,#c9c2b5 35%,#8b8f9a 60%,#d8d6d2 100%)}

/* intro */
.intro{position:absolute;top:760px;left:0;width:1200px;text-align:center}
.intro h1{font-size:30px;font-weight:500;line-height:1.9}
.intro em{font-style:normal;color:var(--pink)}
.intro p{margin-top:28px;font-size:14px;line-height:2.1;color:#555}

/* section titles */
.sec-title{position:absolute;left:0;width:1200px;text-align:center}
.sec-title h2{font-size:30px;font-weight:500}
.sec-title span{display:block;font-size:11px;letter-spacing:3px;color:var(--green);margin-top:4px}
.sec-title i{display:block;width:60px;height:2px;background:var(--green);margin:8px auto 0}
.lead{position:absolute;left:0;width:1200px;text-align:center;font-size:13px;line-height:2;color:#555}

.btn{position:absolute;height:44px;border:1px solid var(--green);color:var(--green);display:flex;align-items:center;justify-content:center;font-size:14px;background:#fff}
.btn::after{content:"";position:absolute;right:16px;width:8px;height:8px;border-top:1px solid var(--green);border-right:1px solid var(--green);transform:rotate(45deg)}

/* voice */
.voice-card{position:absolute;top:1232px;width:236px}
.voice-photo{position:relative;height:220px;background:linear-gradient(180deg,#e9e9e6,#b8b6b0)}
.voice-photo::before{content:"";position:absolute;left:8px;top:0;width:14px;height:100%;background:var(--green);opacity:.6}
.voice-tag{display:inline-block;margin-top:-14px;position:relative;background:#fff;border:1px solid var(--line);font-size:11px;padding:3px 10px}
.voice-title{color:var(--pink);font-size:13px;line-height:1.6;margin-top:8px}
.voice-name{font-size:11px;color:var(--muted);margin-top:8px}

/* service */
.svc-photo{position:absolute;height:270px}
.svc-box{position:absolute;background:#fff;border:1px solid var(--line);box-shadow:0 0 0 10px var(--pale);padding:30px 36px}
.svc-num{width:52px;height:52px;border-radius:50%;border:1px solid #aaa;display:flex;align-items:center;justify-content:center;font-size:16px;margin:0 auto 14px}
.svc-box h3{font-size:19px;font-weight:700;margin-bottom:12px}
.svc-box p{font-size:12px;line-height:1.9;color:#555}

/* blog */
.blog-card{position:absolute;top:3096px;width:238px}
.blog-photo{height:170px;position:relative}
.blog-new{position:absolute;left:10px;top:0;background:var(--pink);color:#fff;font-size:10px;padding:4px 8px}
.blog-cat{display:inline-block;background:var(--green);color:#fff;font-size:10px;padding:2px 10px;margin-top:10px}
.blog-date{font-size:11px;color:var(--muted);margin-top:6px}
.blog-text{font-size:12px;line-height:1.6;margin-top:4px}
.arrow{position:absolute;top:3170px}

/* recruit */
.recruit{left:0;top:3592px;width:1200px;height:350px;background:linear-gradient(90deg,#3e3e3e 0%,#777 45%,#cfc7bd 75%,#8a8580 100%)}
.recruit-copy{position:absolute;top:3660px;left:0;width:1200px;text-align:center;color:#fff}
.recruit-copy h2{font-size:44px;letter-spacing:4px;font-weight:500}
.recruit-copy p{font-size:18px;line-height:1.7;margin-top:6px}
.recruit-btn{position:absolute;top:3840px;left:470px;width:260px;height:44px;border:1px solid #fff;color:#fff;display:flex;align-items:center;justify-content:center;font-size:14px}

/* message */
.msg-photo{left:120px;top:4040px;width:500px;height:420px;background:linear-gradient(135deg,#dcd8d0,#a9a49b 55%,#e2945a)}
.msg-box{position:absolute;left:592px;top:4168px;width:488px;height:304px;background:#fff;border:4px solid var(--green);text-align:center;padding-top:34px}
.msg-box h2{font-size:30px;font-weight:500}
.msg-box p{font-size:14px;line-height:1.8;margin-top:14px}
.msg-box .rep{font-size:13px;margin-top:6px;font-weight:700}

.map{left:0;top:4560px;width:1200px;height:300px;background:linear-gradient(180deg,#e6e6e6,#d6d6d6)}

/* footer */
.site-footer{position:absolute;left:0;top:4860px;width:1200px;height:108px;background:var(--green);color:#fff;padding:16px 120px}
.site-footer .brand{color:#fff;font-size:22px}
.site-footer .brand-dot{background:#fff}
.f-addr{font-size:10px;line-height:1.6;margin-top:6px}
.f-links{position:absolute;right:120px;top:20px;display:flex;gap:10px}
.f-links span{border:1px solid #fff;font-size:11px;padding:4px 14px}
.f-copy{position:absolute;right:120px;top:64px;font-size:10px}
.to-top{position:absolute;left:1030px;top:4800px;width:40px;height:40px;border-radius:50%;background:var(--green)}
</style>
</head>
<body>

<span class="ph hero" role="img" aria-label="講演する代表と会議室の様子、ハロウィン装飾のある窓辺"></span>
<header class="site-header">
  <div class="brand"><span class="brand-dot"></span>Meadowpath</div>
  <nav class="global-nav"><span>会社情報</span><span>サービス</span><span>クライアントの声</span><span>歯科塾</span><span>採用情報</span><span>お問い合わせ</span></nav>
  <div class="phone-box"><small>お気軽にお問い合わせください</small><strong>0120-418-207</strong></div>
</header>

<section class="intro">
  <h1 class="serif">クライアントの<em>“こうしたい”</em>に<br><em>“そこまでやるか”</em>でカタチにする。</h1>
  <p>分かりにくあるものを、スキルや想いをもった私たちが形に。<br>同じように想いで、高いスキルを持った個人や組織と繋がることによって<br>世の中に価値あるものを生み出していく。</p>
</section>

<div class="sec-title serif" style="top:1050px"><h2>クライアントの声</h2><span>VOICE</span><i></i></div>
<p class="lead" style="top:1150px">お手伝いをさせて頂いたみなさんの<br>ご利用後の声を集めて頂きました。</p>

<div class="voice-card" style="left:112px"><div class="voice-photo" role="img" aria-label="スーツ姿のクライアント"></div><span class="voice-tag">株式会社 担当者</span><p class="voice-title">タイトルが入ります。<br>タイトルが入ります。</p><p class="voice-name">氏名　氏名</p></div>
<div class="voice-card" style="left:364px"><div class="voice-photo" role="img" aria-label="白衣姿のクライアント"></div><span class="voice-tag">株式会社 担当者</span><p class="voice-title">タイトルが入ります。<br>タイトルが入ります。</p><p class="voice-name">氏名　氏名</p></div>
<div class="voice-card" style="left:616px"><div class="voice-photo" role="img" aria-label="白衣姿のクライアント"></div><span class="voice-tag">株式会社 担当者</span><p class="voice-title">タイトルが入ります。<br>タイトルが入ります。</p><p class="voice-name">氏名　氏名</p></div>
<div class="voice-card" style="left:868px"><div class="voice-photo" role="img" aria-label="シャツ姿のクライアント"></div><span class="voice-tag">株式会社 担当者</span><p class="voice-title">タイトルが入ります。<br>タイトルが入ります。</p><p class="voice-name">氏名　氏名</p></div>

<div class="btn" style="left:480px;top:1668px;width:360px">詳しく見る</div>

<div class="sec-title serif" style="top:1790px"><h2>サービス</h2><span>SERVICE</span><i></i></div>

<span class="ph svc-photo" style="left:120px;top:1944px;width:480px;background:linear-gradient(135deg,#e4e4e4,#8d8d8d)" role="img" aria-label="グラフ資料を前に打ち合わせする手元"></span>
<div class="svc-box" style="left:628px;top:1970px;width:430px;height:220px;text-align:center"><div class="svc-num">01</div><h3>歯科医院専門コンサルティング</h3><p>医院の経営・集患・人財育成・技術を考慮しながら、目指すゴールへ向けた最適なプランを提案します。</p></div>

<div class="svc-box" style="left:140px;top:2280px;width:440px;height:220px;text-align:center"><div class="svc-num">02</div><h3>ホームページ作成</h3><p>歯科医院の魅力を引き出し、患者さまに伝わるホームページを制作します。運用まで一貫してサポートします。</p></div>
<span class="ph svc-photo" style="left:604px;top:2256px;width:476px;background:linear-gradient(135deg,#5a5f66,#c7c9cc)" role="img" aria-label="パソコンで作業する手元"></span>

<span class="ph svc-photo" style="left:120px;top:2568px;width:480px;background:linear-gradient(135deg,#c2b8a8,#6e6a64)" role="img" aria-label="セミナー会場で話を聞く参加者"></span>
<div class="svc-box" style="left:628px;top:2594px;width:430px;height:220px;text-align:center"><div class="svc-num">03</div><h3>歯科塾（歯科医院のコミュニティ）</h3><p>志を同じくする歯科医院が集まり学び合う場です。経営や技術の情報を共有し、共に成長していきます。</p></div>

<div class="sec-title serif" style="top:2960px"><h2>ブログ</h2><span>BLOG</span><i></i></div>

<svg class="arrow" style="left:130px" width="20" height="40" viewBox="0 0 20 40"><path d="M16 4 L4 20 L16 36" fill="none" stroke="#999" stroke-width="2"/></svg>
<svg class="arrow" style="left:1050px" width="20" height="40" viewBox="0 0 20 40"><path d="M4 4 L16 20 L4 36" fill="none" stroke="#999" stroke-width="2"/></svg>

<div class="blog-card" style="left:208px"><div class="blog-photo" style="background:linear-gradient(135deg,#d9d3c8,#9a9187)" role="img" aria-label="机の上のノートとペン"><span class="blog-new">NEW</span></div><span class="blog-cat">カテゴリー</span><p class="blog-date">2017.00.00</p><p class="blog-text">タイトルが入ります。タイトルが入ります。タイトルが入ります。</p></div>
<div class="blog-card" style="left:480px"><div class="blog-photo" style="background:linear-gradient(135deg,#f0eeea,#b9b4ad)" role="img" aria-label="ノートとスマートフォンのある机"><span class="blog-new">NEW</span></div><span class="blog-cat">カテゴリー</span><p class="blog-date">2017.00.00</p><p class="blog-text">タイトルが入ります。タイトルが入ります。タイトルが入ります。</p></div>
<div class="blog-card" style="left:752px"><div class="blog-photo" style="background:linear-gradient(180deg,#c9dff0,#5f8a3e)" role="img" aria-label="緑の木々と空の風景"></div><span class="blog-cat">カテゴリー</span><p class="blog-date">2017.00.00</p><p class="blog-text">タイトルが入ります。タイトルが入ります。タイトルが入ります。</p></div>

<div class="btn" style="left:480px;top:3414px;width:360px">詳しく見る</div>

<span class="ph recruit" role="img" aria-label="笑顔で働くスタッフたち"></span>
<div class="recruit-copy serif"><h2>RECRUIT</h2><p>一緒に前進しよう<br>あなたが動けば、未来が変わる。</p></div>
<div class="recruit-btn">詳しく見る</div>

<span class="ph msg-photo" role="img" aria-label="講演する代表"></span>
<div class="msg-box">
  <h2 class="serif">Message</h2>
  <p>「困っている人を助けたい」<br>そんな想いでメドウパスは始まった。</p>
  <p class="rep">代表　森川 直人</p>
  <div class="btn" style="left:124px;top:214px;width:232px">詳しく見る</div>
</div>

<span class="ph map" role="img" aria-label="所在地周辺の地図"></span>
<svg class="ph" style="left:484px;top:4640px" width="32" height="44" viewBox="0 0 32 44"><path d="M16 0C7 0 0 7 0 16c0 12 16 28 16 28s16-16 16-28C32 7 25 0 16 0z" fill="#5bb531"/><circle cx="16" cy="16" r="6" fill="#fff"/></svg>
<svg class="to-top" width="40" height="40" viewBox="0 0 40 40"><path d="M13 23 L20 16 L27 23" fill="none" stroke="#fff" stroke-width="2"/></svg>

<footer class="site-footer">
  <div class="brand"><span class="brand-dot"></span>Meadowpath</div>
  <p class="f-addr">株式会社メドウパス<br>〒000-0000 東京都〇〇区〇〇 0-0-0<br>TEL 0120-418-207</p>
  <div class="f-links"><span>お問い合わせ</span><span>採用情報</span></div>
  <p class="f-copy">Copyright © Meadowpath All Rights Reserved.</p>
</footer>

</body>
</html>
```